Need Letterhead Design & Matching Business Card

I have a logo that I love already. But the letterhead is less than appealing and boring. I'd like a design for my letterhead which I will match with business cards. Also, I'd like to have used fonts that are generally available, as my current letterhead uses a font named "SPACE" which nobody has unless they download it...so when a Word version is forwarded, it looks awful on the receiver's screed due to not having the font. That being said, modern is the look we like and are going for.

My business is "Halloran Brightmoor PC" - a law firm specializing in representing people who have suffered catastrophic injuries or death (plane, auto, train crashes etc.).

See attached letterhead, which has all of the pertinent information. My logo is also attached in various formats.

```html
<!DOCTYPE html>
<html lang="en">
<head>
<meta charset="utf-8">
<title>Halloran Brightmoor PC — Letterhead</title>
<link href="https://fonts.googleapis.com/css2?family=Inter:wght@300;400;600&display=swap" rel="stylesheet">
<style>
  :root {
    --backdrop: #dcdce0;
    --paper: #ffffff;
    --ink: #1c1c1c;
    --body-ink: #2b2b2b;
    --rule: #3a3a3a;
    --divider: #b5b5b5;
    --mark: #262524;
    --signature-tone: #e6e6f2;
  }
  * { margin: 0; padding: 0; box-sizing: border-box; }
  html, body {
    width: 1200px; height: 1200px; overflow: hidden;
    background: var(--backdrop);
    font-family: "Inter", Arial, sans-serif;
    color: var(--body-ink);
  }
  .letterhead {
    position: absolute; left: 167px; top: 40px;
    width: 865px; height: 1120px;
    background: var(--paper);
  }
  .firm-name {
    position: absolute; left: 74px; top: 76px;
    font-weight: 300; font-size: 36px; line-height: 34px;
    letter-spacing: -0.5px; color: var(--ink); text-transform: uppercase;
  }
  .firm-square {
    position: absolute; left: 709px; top: 69px;
    width: 83px; height: 83px; background: var(--mark);
  }
  .rule { position: absolute; left: 74px; width: 718px; height: 1px; background: var(--rule); }
  .rule--top { top: 174px; }
  .rule--bottom { top: 1041px; }
  .recipient, .letter-body, .closing, .signatory {
    position: absolute; left: 78px; width: 714px;
    font-size: 12px; line-height: 15px; font-weight: 300;
  }
  .recipient { top: 241px; font-style: normal; }
  .letter-body { top: 366px; text-align: justify; letter-spacing: -0.2px; }
  .letter-body p { margin-bottom: 15px; }
  .closing { top: 746px; }
  .signature {
    position: absolute; left: 74px; top: 776px;
    width: 143px; height: 60px; background: var(--signature-tone); border-radius: 4px;
  }
  .signatory { top: 850px; }
  .signatory strong { font-weight: 600; color: var(--ink); }
  .footer {
    position: absolute; left: 74px; top: 1055px; width: 718px;
    display: flex; justify-content: space-between; align-items: stretch;
  }
  .footer-col {
    font-size: 10.5px; line-height: 14px; font-weight: 400; color: var(--ink);
    white-space: nowrap;
  }
  .footer-col strong { font-weight: 600; }
  .footer-divider { width: 1px; height: 26px; background: var(--divider); flex: none; }
</style>
</head>
<body>
  <main class="letterhead">
    <header>
      <h1 class="firm-name">Halloran<br>Brightmoor PC</h1>
      <div class="firm-square" aria-hidden="true"></div>
    </header>
    <div class="rule rule--top"></div>

    <address class="recipient">
      Mr. Everett Lindqvist<br>
      President and CEO<br>
      NovaGenix LLC.<br>
      2210 Meridian Avenue, Suite 3100<br>
      Riverton, NY 10988
    </address>

    <section class="letter-body">
      <p>Dear Mr. Lindqvist:</p>
      <p>As Chairperson of the Corporate Conscience Campaign - Helping the Homeless in New York, I am writing this to thank you personally for your company's support in last month's fund-raising effort.</p>
      <p>As I indicated when we spoke on the phone two weeks ago, the campaign was considered a resounding success, raising a total of $1.65 million to-date, significantly exceeding our target of $1 million. Some donations are still trickling in, so we could end up close to a total of $2 million.</p>
      <p>NovaGenix was an influential leader throughout the entire three-month campaign. In fact, we couldn't have succeeded without the generous support of your company, both financially, and through your organizational and administrative assistance. Your Team Leader, Marisol Treadwell was particularly impressive, going above and beyond what we could have expected of someone performing as a volunteer while continuing on with her day-to-day duties. Please convey my special thanks to Marisol.</p>
      <p>I would also ask you to convey my sincere thanks and congratulations to all of those other people in your company who contributed in any way to the Helping the Homeless Campaign. Please tell them that the sum of their contributions resulted in a major success that they should all be proud of taking part in.</p>
      <p>I believe that the 27 companies that participated in this effort have set a new standard for social responsibility in this community, and have set a powerful example that will inspire other companies and organizations to do the same.</p>
      <p>I look forward to seeing you at the Mayor's special thank you reception next month.</p>
    </section>

    <p class="closing">Yours sincerely,</p>
    <div class="signature" role="img" aria-label="Handwritten signature in blue ink"></div>
    <p class="signatory"><strong>Gideon Harcourt</strong><br>Fundraising Chair</p>

    <div class="rule rule--bottom"></div>
    <footer class="footer">
      <div class="footer-col">Halloran Brightmoor PC<br>www.<strong>halloranbrightmoor</strong>.com</div>
      <div class="footer-divider"></div>
      <div class="footer-col"><strong>R. CORWIN HALLORAN</strong>, Esq.<br>President</div>
      <div class="footer-divider"></div>
      <div class="footer-col">4820 Brightmoor Ave., Suite 700<br>Lakeview, CA 90555</div>
      <div class="footer-divider"></div>
      <div class="footer-col">T: (555) 014-2290<br>E: rc@halloranbrightmoor.com</div>
    </footer>
  </main>
</body>
</html>
```